Business Card Design

5* Hotel Property based on an island in Greece

My position is aparta from being a director, i'm on the accounts payable too, not sure how this should be stated, with a comma or "/"?

Sorry about the uploaded logo, it was a mistaken one!

There's also need to be added this  www.corvanteholdings.com on the back side of the card!

Also need to have the logo of the corvante holdings which can be found in a second on the brief! Thank you guys, irini

Industry/Entity Type

Business

Contact Information for Business Card

VERISTOKA PELLA Hotel
Irini Dravetsou
Director, AP Dept.

www.veristoka.gr
Peltira Island 85300
Greece

irinidravetsou@fenmail.com
+306951273064

```html
<!DOCTYPE html>
<html lang="en">
<head>
<meta charset="utf-8">
<title>Veristoka Pella Hotel – Business Card</title>
<link rel="stylesheet" href="https://fonts.googleapis.com/css2?family=Questrial&display=swap">
<style>
  :root {
    --frame-light: #3ba9e2;
    --frame-dark: #2474bf;
    --brand-blue: #2c86c9;
    --text-grey: #3a3a3a;
    --logo-grey: #7d7d7d;
    --pattern-blue: #8fa8d6;
    --back-field: #eeeced;
    --page: #ffffff;
  }
  * { box-sizing: border-box; margin: 0; padding: 0; }
  html, body {
    width: 1200px; height: 369px; overflow: hidden;
    background: var(--page);
    font-family: "Questrial", "Helvetica Neue", Arial, sans-serif;
  }
  .canvas { position: relative; width: 1200px; height: 369px; }

  .card { position: absolute; }
  .card-front {
    left: 66px; top: 27px; width: 494px; height: 323px;
    border-style: solid;
    border-width: 15px 17px 23px 26px;
    border-color: var(--frame-light) var(--frame-dark) var(--frame-dark) var(--frame-light);
    background: #fff;
    box-shadow: 0 2px 4px rgba(0,0,0,.25);
  }
  .card-back {
    left: 643px; top: 20px; width: 500px; height: 332px;
    border-style: solid;
    border-width: 13px 13px 17px 14px;
    border-color: var(--frame-dark) var(--frame-light) var(--frame-light) var(--frame-dark);
    background: var(--back-field);
    box-shadow: 0 2px 4px rgba(0,0,0,.25);
  }

  .corner-pattern { position: absolute; }
  .corner-pattern.top-left { left: 0; top: 0; }
  .corner-pattern.bottom-right { right: 0; bottom: 0; }

  .brand { position: absolute; display: flex; align-items: center; }
  .brand-dot { border-radius: 50%; background: var(--brand-blue); flex: none; }
  .brand-name { color: var(--logo-grey); line-height: 1.05; letter-spacing: .5px; }

  .card-front .brand { left: 118px; top: 36px; }
  .card-front .brand-dot { width: 46px; height: 46px; margin-right: 12px; }
  .card-front .brand-name { font-size: 17px; }

  .card-back .brand { left: 75px; top: 100px; }
  .card-back .brand-dot { width: 86px; height: 86px; margin-right: 16px; }
  .card-back .brand-name { font-size: 28px; }

  .group-line {
    position: absolute; left: 0; right: 0; bottom: 22px;
    display: flex; justify-content: space-between; align-items: center;
    padding: 0 28px;
    color: var(--logo-grey); font-size: 13px; letter-spacing: .6px;
  }
  .group-brand { display: flex; align-items: center; }
  .group-mark { width: 10px; height: 10px; background: var(--brand-blue); margin-right: 7px; }

  .contact { position: absolute; left: 126px; top: 108px; }
  .person-name { color: var(--brand-blue); font-size: 25px; line-height: 30px; }
  .person-role { color: var(--brand-blue); font-size: 19px; line-height: 24px; letter-spacing: .3px; }
  .phone { color: var(--text-grey); font-size: 19px; line-height: 30px; letter-spacing: 1.4px; }
  .email { color: var(--text-grey); font-size: 15px; line-height: 26px; margin-top: 2px; }
  .address { color: var(--text-grey); font-size: 12px; line-height: 24px; }
  .website { color: var(--text-grey); font-size: 14px; line-height: 20px; letter-spacing: 2.6px; }
</style>
</head>
<body>
<main class="canvas">

  <section class="card card-front">
    <svg class="corner-pattern top-left" width="120" height="120" viewBox="0 0 120 120" role="img" aria-label="Geometric blue lattice pattern corner">
      <polygon points="0,0 120,0 0,120" fill="var(--pattern-blue)"/>
    </svg>
    <svg class="corner-pattern bottom-right" width="120" height="120" viewBox="0 0 120 120" role="img" aria-label="Geometric blue lattice pattern corner">
      <polygon points="120,0 120,120 0,120" fill="var(--pattern-blue)"/>
    </svg>

    <div class="brand">
      <span class="brand-dot"></span>
      <span class="brand-name">VERISTOKA PELLA<br>Hotel</span>
    </div>

    <div class="contact">
      <p class="person-name">Irini Dravetsou</p>
      <p class="person-role">Director, AP Dept</p>
      <p class="phone">+306951273064</p>
      <p class="email">irinidravetsou@fenmail.com</p>
      <p class="address">Peltira Island 85300 Greece</p>
      <p class="website">www.veristoka.gr</p>
    </div>
  </section>

  <section class="card card-back" aria-label="Back of card with faint geometric lattice pattern, hotel name and group details">
    <div class="brand">
      <span class="brand-dot"></span>
      <span class="brand-name">VERISTOKA PELLA<br>Hotel</span>
    </div>
    <div class="group-line">
      <span class="group-brand"><span class="group-mark"></span>corvante holdings</span>
      <span class="group-web">www.corvanteholdings.com</span>
    </div>
  </section>

</main>
</body>
</html>
```